Innovative Educational Technology Startup needs Business Cards!

"Campus Horizon" is an all-in-one, social profile based, online portal for Companies and Students to connect and carry out their brand ambassadorship tasks and requirements. The service allows for companies to more efficiently deploy brand ambassadorship opportunities to the millions of students actively seeking on-campus work experience.

Both educational and corporate tied into one (please keep that in mind for design purposes)
Updates

Project Deadline Extended
Reason: Need time to provide feedback to the several great designs that have been created! Thanks for the patience of one more day!

Target Market(s)

Those who get the card will more than likely be business men and working adults, but many educational instructors, professors, students, marketers, and propoective collegiate students will be the main target for these cards.

Industry/Entity Type

Business

Requirements
Must have
• Our Icon-Sized Logo (CH) must be a focus in regards to imagery.
• Color scheme must be Tiffany Blue/Black/White..(base of the card either white or black).
• www.campushorizonhub.com located somewhere on it, but not the main point of the card. (Logo is for that)
Should not have
• Childish or Tech-Only appeal.
• Basic font.
• Rather there be as little asymmetry in the card shape as possible. (curved edges is fine)

```html
<!DOCTYPE html>
<html lang="en">
<head>
<meta charset="utf-8">
<title>Campus Horizon – Business Card</title>
<link rel="stylesheet" href="https://fonts.googleapis.com/css2?family=Didact+Gothic&display=swap">
<style>
  :root {
    --card-white: #ffffff;
    --tiffany-blue: #0abab5;
    --ink-black: #1a1a1a;
    --frame-grey: #8a8a8a;
    --outer-grey: #9a9a9a;
  }
  html, body {
    margin: 0;
    padding: 0;
    width: 1200px;
    height: 748px;
    overflow: hidden;
    background: var(--card-white);
  }
  .canvas {
    position: relative;
    width: 1200px;
    height: 748px;
    background: var(--card-white);
  }
  .card-shapes {
    position: absolute;
    inset: 0;
    width: 1200px;
    height: 748px;
  }
  .outer-border { fill: none; stroke: var(--outer-grey); stroke-width: 1; }
  .trim-line { fill: none; stroke: var(--frame-grey); stroke-width: 1; }
  .side-band { fill: var(--tiffany-blue); stroke: var(--ink-black); stroke-width: 0.6; }
  .brand-ring { fill: none; stroke: var(--tiffany-blue); stroke-width: 4; }
  .brand-name {
    position: absolute;
    left: 0;
    width: 1220px;
    top: 295px;
    margin: 0;
    text-align: center;
    font-family: "Didact Gothic", sans-serif;
    font-weight: 400;
    font-size: 88px;
    line-height: 1;
    letter-spacing: 1px;
    color: var(--tiffany-blue);
  }
  .web-address {
    position: absolute;
    left: 0;
    width: 1220px;
    top: 432px;
    margin: 0;
    text-align: center;
    font-family: "Didact Gothic", sans-serif;
    font-weight: 400;
    font-size: 24px;
    line-height: 1;
    letter-spacing: 2px;
    color: var(--ink-black);
  }
</style>
</head>
<body>
  <main class="canvas">
    <svg class="card-shapes" viewBox="0 0 1159 722" preserveAspectRatio="none" aria-hidden="true">
      <rect class="outer-border" x="0.5" y="0.5" width="1158" height="721"/>
      <rect class="trim-line" x="66.5" y="52.5" width="1034" height="615"/>
      <polygon class="side-band" points="66,73 99,87 99,450 66,436"/>
      <polygon class="side-band" points="1068,274 1101,260 1101,623 1068,637"/>
      <circle class="brand-ring" cx="583" cy="165" r="86"/>
    </svg>
    <h1 class="brand-name">Campus Horizon</h1>
    <p class="web-address">www.campushorizonhub.com</p>
  </main>
</body>
</html>
```